Business Card Design Project

Need a business card with logo that is attached.
Company name: Tolmen Brisk Solutions, LLC
My name: Lorna Tolmen
Title: President
Phone number: 703-555-0148
Email: ltolmen@tolmenbrisksolutions.example
web site: www.tolmenbrisksolutions.example

Industry/Entity Type

Business

```html
<!DOCTYPE html>
<html lang="en">
<head>
<meta charset="utf-8">
<title>Tolmen Brisk Solutions, LLC — Business Card</title>
<link rel="stylesheet" href="https://fonts.googleapis.com/css2?family=Tinos&family=Arimo:wght@400&display=swap">
<style>
  :root {
    --page: #e9e6e1;
    --card-top: #4d4d50;
    --card-bottom: #38383b;
    --blue: #2a9ee0;
    --blue-deep: #1663b8;
    --teal: #1fb89a;
    --sky: #3fb4e6;
    --white: #ffffff;
  }
  * { box-sizing: border-box; margin: 0; padding: 0; }
  html, body { width: 1200px; height: 1056px; overflow: hidden; background: var(--page); }
  .canvas { position: relative; width: 1200px; height: 1056px; display: flex; align-items: center; justify-content: center; }
  .card {
    position: relative; width: 1050px; height: 600px; border-radius: 28px; overflow: hidden;
    background: linear-gradient(160deg, var(--card-top), var(--card-bottom));
    box-shadow: 0 20px 50px rgba(0,0,0,.25);
  }
  .brand { position: absolute; left: 70px; top: 170px; display: flex; align-items: center; gap: 30px; }
  .brand-mark { width: 120px; height: 120px; border-radius: 50%; background: var(--sky); flex: none; }
  .brand-divider { width: 2px; height: 140px; background: var(--teal); }
  .brand-name {
    font-family: "Tinos", serif; color: var(--sky); font-size: 40px; line-height: 1.1;
    letter-spacing: 2px; text-transform: uppercase;
  }
  .rule { position: absolute; height: 3px; }
  .rule-brand { left: 90px; top: 350px; width: 520px; background: var(--sky); }
  .rule-person { right: 70px; top: 190px; width: 380px; background: var(--teal); }
  .person { position: absolute; right: 70px; top: 50px; text-align: right; font-family: "Tinos", serif; }
  .person-name { color: var(--sky); font-size: 46px; }
  .person-title { color: var(--teal); font-size: 32px; margin-top: 8px; }
  .contact { position: absolute; top: 400px; display: flex; align-items: center; gap: 16px;
    font-family: "Arimo", sans-serif; font-size: 27px; color: var(--sky); }
  .contact-phone { left: 90px; }
  .contact-email { right: 60px; }
  .icon { width: 38px; height: 38px; flex: none; }
  .web-band {
    position: absolute; left: 0; right: 0; bottom: 0; height: 100px;
    background: linear-gradient(90deg, var(--blue-deep), var(--blue));
    display: flex; align-items: center; justify-content: flex-end; padding-right: 120px; gap: 16px;
    font-family: "Arimo", sans-serif; font-size: 32px; color: var(--white);
  }
</style>
</head>
<body>
<main class="canvas">
  <section class="card">
    <div class="brand">
      <span class="brand-mark"></span>
      <span class="brand-divider"></span>
      <p class="brand-name">Tolmen Brisk<br>Solutions<br>LLC</p>
    </div>
    <span class="rule rule-brand"></span>

    <div class="person">
      <p class="person-name">Lorna Tolmen</p>
      <p class="person-title">President</p>
    </div>
    <span class="rule rule-person"></span>

    <p class="contact contact-phone">
      <svg class="icon" viewBox="0 0 40 40" aria-hidden="true">
        <circle cx="20" cy="20" r="19" fill="#3fb4e6"/>
        <path d="M14 11c1-1 2.5-1 3 .5l1.5 3.5c.4 1-.3 1.8-1 2.4 1 2.3 2.8 4.2 5 5.3.6-.7 1.4-1.4 2.4-1l3.5 1.5c1.5.6 1.5 2 .5 3l-1.5 1.5c-5 1.5-15-8.5-13.4-13.6z" fill="#3a3a3d"/>
      </svg>
      703-555-0148
    </p>
    <p class="contact contact-email">
      <svg class="icon" viewBox="0 0 40 40" aria-hidden="true">
        <circle cx="20" cy="20" r="19" fill="#3fb4e6"/>
        <rect x="10" y="13" width="20" height="14" rx="2" fill="#3a3a3d"/>
        <path d="M10.5 14l9.5 7 9.5-7" stroke="#3fb4e6" stroke-width="2" fill="none"/>
      </svg>
      ltolmen@tolmenbrisksolutions.example
    </p>

    <div class="web-band">
      <svg class="icon" viewBox="0 0 40 40" aria-hidden="true">
        <g fill="none" stroke="#ffffff" stroke-width="2.5">
          <circle cx="20" cy="20" r="16"/>
          <ellipse cx="20" cy="20" rx="7" ry="16"/>
          <path d="M4 20h32M7 12h26M7 28h26"/>
        </g>
      </svg>
      www.tolmenbrisksolutions.example
    </div>
  </section>
</main>
</body>
</html>
```